AMAZING FLYERS, POSTCARDS, AND MARKETING!!!! - Northgable Shingle & Eave Works, LLC

This project will be for Northgable Shingle & Eave Works, LLC. The flyers and postcards will be used to saturate the Alaska market with our services, and get our name and logo out there for people to remember. We plan to send the flyers and postcards out in a broad scale (both door to door and mail out). We want to send out flyers to realty and property management businesses to introduce our roofing company, and to advertise our services. We would also like to have another version, or the ability to edit the text of the final product to send out the same materials to residential clients (homeowners) by just changing the text slightly to better fit that market.
We have a logo, but need something put together that we can tri-fold and mail out to potential clients. We are planning to do some postcards as well. We would like the option to mail them or bring them to people in person.
We are a locally owned roofing and repair company in Alaska. We would like something professional that will capture their attention and show the potential of working with our company. I included some detailed information about our company and some pictures below of our work trailer and a before/after on a recent project. I also attached our logo files. Please go through the attached data and let us know what you come up with to stir up the marketing aspect of our company. Thank you for your time and consideration.

Project Deadline Extended
Reason: Allowing additional time for designers to submit/resubmit their flyer/postcard ideas based on inquiries and feedback.

Target Market(s)

1.) Homeowners are the first target market.
2.)Realtors and Property Management companies are the second market

Industry/Entity Type

Marketing

Contact Information for Business Card

Include the logo and contact information for our company. These business cards will be for the Owner, Harold Vemstrup, II.
There is also a Co-Owner, Wanda Vemstrup, so we will need the ability to print business cards for each owner. Need to be able to change the title/name and phone number for Wanda's contact information please. Contact information, license #, and logo information on one side of the card. Please tell the potential client a little about us on the back of the card by utilizing the attached information.

Requirements
Must have
• Pertinent information about our company and listed in the company information attachment. Attention getting details and design work. Professional in appearance and unique to our company to set us above the general advertisers in this industry.
Nice to have
• Something that sets our flyers apart from the ones people get every day. We want to rise above normal with our advertising.
Should not have
• Nothing plain and boring.

```html
<!DOCTYPE html>
<html lang="en">
<head>
<meta charset="utf-8">
<title>Northgable Shingle &amp; Eave Works – Tri-fold Brochure</title>
<link rel="stylesheet" href="https://fonts.googleapis.com/css2?family=Archivo+Black&family=Questrial&family=Roboto+Condensed:wght@400;700&family=Montserrat:wght@500;600&display=swap">
<style>
  :root {
    --ink: #0d0d0d;
    --paper: #ffffff;
    --silver-light: #e9e9e9;
    --silver-mid: #a8a8a8;
    --silver-dark: #4a4a4a;
    --stage: #eeeeee;
    --icon-blue: #1f5fbf;
  }
  * { box-sizing: border-box; margin: 0; padding: 0; }
  html, body { width: 1200px; height: 840px; overflow: hidden; background: var(--stage); }
  .brochure {
    position: absolute; left: 105px; top: 30px;
    width: 990px; height: 780px; display: flex;
    box-shadow: 0 6px 24px rgba(0,0,0,.18);
  }
  .panel { position: relative; width: 330px; height: 780px; overflow: hidden; }
  .panel > svg { position: absolute; inset: 0; }

  /* Inside info panel */
  .panel--info { background: var(--ink); color: var(--paper); }
  .info-copy { position: absolute; left: 30px; top: 26px; width: 270px; }
  .info-copy h2 {
    font-family: "Archivo Black", sans-serif; font-size: 16.5px; letter-spacing: .3px;
    padding-bottom: 4px; border-bottom: 2px solid var(--paper); display: inline-block; margin-bottom: 16px;
  }
  .info-copy p {
    font-family: "Questrial", sans-serif; font-size: 11px; line-height: 1.3;
    text-align: justify; margin-bottom: 8px;
  }

  /* Contact panel */
  .panel--contact { background: var(--paper); }
  .pill {
    position: absolute; left: 50%; transform: translateX(-50%);
    background: var(--ink); color: var(--paper); border-radius: 14px;
    font-family: "Roboto Condensed", sans-serif; white-space: nowrap;
    box-shadow: 0 4px 5px rgba(0,0,0,.35);
  }
  .pill--title { top: 198px; font-size: 21px; padding: 4px 14px; }
  .pill--web { top: 470px; font-size: 15px; font-weight: 700; padding: 5px 16px; }
  .contact-list {
    position: absolute; top: 250px; left: 0; width: 100%; list-style: none;
    font-family: "Roboto Condensed", sans-serif; font-weight: 700; font-size: 17px; color: var(--ink);
  }
  .contact-list li { display: flex; align-items: center; justify-content: center; gap: 8px; height: 23px; }
  .contact-list svg { width: 11px; height: 11px; fill: var(--icon-blue); }
  .brand-name {
    position: absolute; left: 0; width: 100%; text-align: center;
    font-family: "Montserrat", sans-serif; font-weight: 600; text-transform: uppercase; letter-spacing: 1px;
  }
  .brand-name--contact { top: 370px; font-size: 15px; line-height: 1.35; color: var(--ink); }
  .brand-mark { display: block; width: 12px; height: 12px; background: var(--ink); margin: 0 auto 8px; }

  /* Cover panel */
  .panel--cover { background: var(--ink); }
  .brand-name--cover { top: 52px; font-size: 16px; line-height: 1.35; color: var(--paper); }
  .brand-name--cover .brand-mark { background: var(--paper); }
  .cover-headline { position: absolute; left: 0; top: 598px; width: 100%; font-family: "Montserrat", sans-serif; color: var(--paper); }
  .cover-headline .lead { font-weight: 600; font-size: 33px; padding-left: 30px; letter-spacing: .5px; }
  .cover-headline .band {
    margin-top: 6px; background: var(--paper); color: var(--ink);
    font-weight: 500; font-size: 27px; padding: 2px 0 2px 24px;
  }
  .cover-headline .tail { font-weight: 500; font-size: 20px; padding: 6px 0 0 34px; }
</style>
</head>
<body>
<main class="brochure">

  <section class="panel panel--info">
    <svg viewBox="0 0 330 780" width="330" height="780">
      <defs>
        <linearGradient id="infoBand" x1="0" y1="0" x2="1" y2="0">
          <stop offset="0" stop-color="#f2f2f2"/><stop offset="1" stop-color="#555"/>
        </linearGradient>
        <linearGradient id="houseA" x1="0" y1="0" x2="0" y2="1">
          <stop offset="0" stop-color="#b8c6d2"/><stop offset=".45" stop-color="#9a9c9c"/><stop offset=".75" stop-color="#6f8a4c"/><stop offset="1" stop-color="#5e5e5e"/>
        </linearGradient>
      </defs>
      <polygon points="0,582 330,448 330,468 0,606" fill="url(#infoBand)"/>
      <polygon role="img" aria-label="Photo of a finished single-storey house with driveway and lawn" points="0,606 330,468 330,780 0,780" fill="url(#houseA)"/>
    </svg>
    <div class="info-copy">
      <h2>WHAT IS LOREM IPSUM?</h2>
      <p>Lorem Ipsum is simply dummy text of the printing and typesetting industry. Lorem Ipsum has been the industry's standard dummy text ever since the 1500s, when an unknown printer took a galley of type and scrambled it to make a type specimen book. It has survived not only five centuries, but also the leap into electronic typesetting, remaining essentially unchanged.</p>
      <p>It was popularised in the 1960s with the release of Letraset sheets containing Lorem Ipsum passages, and more recently with desktop publishing software like Aldus PageMaker including versions of Lorem Ipsum.<br>Contrary to popular belief, Lorem Ipsum is not simply random text. It has roots in a piece of classical Latin literature from 45 BC, making it over 2000 years old. Lorem Ipsum comes from sections 1.10.32 and 1.10.33 of "de Finibus Bonorum et Malorum" (The Extremes of Good and Evil) by Cicero, written in 45 BC.</p>
    </div>
  </section>

  <section class="panel panel--contact">
    <svg viewBox="0 0 330 780" width="330" height="780">
      <defs>
        <linearGradient id="roof" x1="0" y1="0" x2="0" y2="1">
          <stop offset="0" stop-color="#8c8c8c"/><stop offset=".7" stop-color="#c9c9c9"/><stop offset="1" stop-color="#ffffff"/>
        </linearGradient>
        <linearGradient id="floor" x1="0" y1="0" x2="1" y2="0">
          <stop offset="0" stop-color="#b0b0b0"/><stop offset=".5" stop-color="#f4f4f4"/><stop offset="1" stop-color="#6a6a6a"/>
        </linearGradient>
        <linearGradient id="trailer" x1="0" y1="0" x2="0" y2="1">
          <stop offset="0" stop-color="#c0392b" stop-opacity=".35"/><stop offset=".2" stop-color="#1a1a1a"/><stop offset="1" stop-color="#111"/>
        </linearGradient>
      </defs>
      <rect role="img" aria-label="Photo of a newly shingled grey roof" x="0" y="0" width="330" height="190" fill="url(#roof)"/>
      <polygon points="0,640 330,610 330,780 0,780" fill="url(#floor)"/>
      <rect role="img" aria-label="Photo of the company work trailer with ladder rack" x="22" y="540" width="300" height="150" rx="6" fill="url(#trailer)"/>
    </svg>
    <div class="pill pill--title">Contact Information</div>
    <ul class="contact-list">
      <li><svg viewBox="0 0 24 24"><path d="M6.6 10.8a15 15 0 0 0 6.6 6.6l2.2-2.2c.3-.3.7-.4 1-.2 1.1.4 2.3.6 3.6.6.6 0 1 .4 1 1V20c0 .6-.4 1-1 1A17 17 0 0 1 3 4c0-.6.4-1 1-1h3.5c.6 0 1 .4 1 1 0 1.3.2 2.5.6 3.6.1.3 0 .7-.2 1z"/></svg>xxx-xxxx-xxx</li>
      <li><svg viewBox="0 0 24 24"><path d="M2 5h20v14H2zM4 7v.5l8 5 8-5V7l-8 5z"/></svg>your@emailid.com</li>
      <li><svg viewBox="0 0 24 24"><path d="M12 2a7 7 0 0 0-7 7c0 5 7 13 7 13s7-8 7-13a7 7 0 0 0-7-7zm0 9.5a2.5 2.5 0 1 1 0-5 2.5 2.5 0 0 1 0 5z"/></svg>yor address here</li>
    </ul>
    <div class="brand-name brand-name--contact"><span class="brand-mark"></span>Northgable Shingle<br>&amp; Eave Works, LLC</div>
    <div class="pill pill--web">www.northgableworks.com</div>
  </section>

  <section class="panel panel--cover">
    <svg viewBox="0 0 330 780" width="330" height="780">
      <defs>
        <linearGradient id="silverL" x1="0" y1="0" x2="1" y2="0">
          <stop offset="0" stop-color="#ececec"/><stop offset="1" stop-color="#6a6a6a"/>
        </linearGradient>
        <linearGradient id="silverR" x1="1" y1="0" x2="0" y2="0">
          <stop offset="0" stop-color="#ececec"/><stop offset="1" stop-color="#6a6a6a"/>
        </linearGradient>
        <linearGradient id="houseB" x1="0" y1="0" x2="0" y2="1">
          <stop offset="0" stop-color="#c9d6e0"/><stop offset=".3" stop-color="#8f9a80"/><stop offset=".6" stop-color="#9a9fa3"/><stop offset="1" stop-color="#5d5d5d"/>
        </linearGradient>
      </defs>
      <polygon points="0,150 330,138 330,160 0,172" fill="#fff"/>
      <polygon points="0,160 170,190 0,290" fill="url(#silverL)"/>
      <polygon points="330,150 170,190 330,250" fill="url(#silverR)"/>
      <polygon role="img" aria-label="Photo of a grey house with red door and new roof" points="0,290 170,190 330,250 330,560 170,490 0,580" fill="url(#houseB)"/>
      <polygon points="0,580 170,490 330,560 330,572 170,506 0,594" fill="#fff"/>
    </svg>
    <div class="brand-name brand-name--cover"><span class="brand-mark"></span>Northgable Shingle<br>&amp; Eave Works, LLC</div>
    <div class="cover-headline">
      <div class="lead">LOREM IPSUM</div>
      <div class="band">IS SIMPLY DUMMY</div>
      <div class="tail">TEXT OF THE PRINTING</div>
    </div>
  </section>

</main>
</body>
</html>
```